Design eines Praxisschilds für Hausarztpraxis
Zielgruppe
Hausarztpraxis, Zielgruppe sind die Bewohner vor Ort, bodenständig
Aufgabenstellung
Praxisschild entwerfen, es soll schlicht sein. Das angefügte Logo bitte verwenden, ggf. auch nur das Symbol ohne Namen verwenden und den Namen extra in schwarz aufführen.
Farben:
- schwarz
- Pantone 13-0645 Limeade
- Pantone 7726
Text:
Dr. med. Jonas Walbrecht
Facharzt für Innere Medizin
Facharzt für Allgemeinmedizin
Sprechzeiten:
Montag bis Freitag 07:30 – 12:00 Uhr
Dienstag und Donnerstag 17:00 – 19:00 Uhr
und nach Vereinbarung
Tel: 0761 83172
www.hausarzt-beispielau.de
Format quer (die Maße sind leider vorgegeben): 55,7 cm x 42,8 cm

```html
<!DOCTYPE html>
<html lang="de">
<head>
<meta charset="utf-8">
<title>Praxisschild – Dr. med. Jonas Walbrecht</title>
<link rel="stylesheet" href="https://fonts.googleapis.com/css2?family=Hind:wght@500;600&display=swap">
<style>
  :root {
    --lime: #d4d862;
    --green: #267a50;
    --black: #111111;
    --white: #ffffff;
    --grey: #b9b9b9;
  }
  * { margin: 0; padding: 0; box-sizing: border-box; }
  html, body { width: 1200px; height: 922px; overflow: hidden; }
  body {
    background: var(--lime);
    font-family: "Hind", Arial, sans-serif;
    position: relative;
  }
  .sign-panel {
    position: absolute;
    left: 39px; top: 73px;
    width: 1121px; height: 774px;
    background: var(--white);
  }
  .brand-dot {
    position: absolute;
    left: 92px; top: 92px;
    width: 188px; height: 188px;
    border-radius: 50%;
    background: var(--lime);
  }
  .brand-divider {
    position: absolute;
    left: 343px; top: 92px;
    width: 2px; height: 190px;
    background: var(--green);
  }
  .doctor-name {
    position: absolute;
    left: 380px; top: 104px;
    font-size: 54px;
    font-weight: 600;
    line-height: 1;
    color: var(--black);
    white-space: nowrap;
    letter-spacing: -0.5px;
  }
  .practice-tagline {
    position: absolute;
    left: 382px; top: 170px;
    font-size: 25px;
    font-weight: 500;
    line-height: 1;
    letter-spacing: 7px;
    color: var(--green);
    white-space: nowrap;
  }
  .specialty {
    position: absolute;
    left: 382px;
    font-size: 22px;
    font-weight: 500;
    line-height: 1;
    color: var(--green);
    white-space: nowrap;
  }
  .specialty.internal { top: 218px; }
  .specialty.general { top: 250px; }
  .hours-title {
    position: absolute;
    left: 0; width: 1200px; top: 322px;
    text-align: center;
    font-size: 32px;
    font-weight: 600;
    letter-spacing: 13px;
    color: var(--lime);
  }
  .hours-title .colon { color: var(--grey); }
  .hours-line {
    position: absolute;
    left: 0; width: 1200px;
    text-align: center;
    font-size: 48px;
    font-weight: 600;
    line-height: 1;
    color: var(--green);
  }
  .hours-line.weekdays { top: 398px; }
  .hours-line.evenings { top: 517px; }
  .hours-line.appointment { top: 636px; }
  .contact-line {
    position: absolute;
    left: 0; width: 1200px;
    text-align: center;
    font-size: 31px;
    font-weight: 600;
    line-height: 1;
    color: var(--green);
  }
  .contact-line.phone { top: 748px; }
  .contact-line.web { top: 792px; }
</style>
</head>
<body>
  <div class="sign-panel"></div>

  <div class="brand-dot"></div>
  <div class="brand-divider"></div>
  <div class="doctor-name">Dr. med. Jonas Walbrecht</div>
  <div class="practice-tagline">IHR HAUSARZT IN BEISPIELAU</div>
  <div class="specialty internal">Facharzt für Innere Medizin</div>
  <div class="specialty general">Facharzt für Allgemeinmedizin</div>

  <div class="hours-title">SPRECHZEITEN<span class="colon">:</span></div>

  <div class="hours-line weekdays">Montag bis Freitag 07:30 – 12:00 Uhr</div>
  <div class="hours-line evenings">Dienstag und Donnerstag 17:00 – 19:00 Uhr</div>
  <div class="hours-line appointment">und nach Vereinbarung</div>

  <div class="contact-line phone">Tel: 0761 83172</div>
  <div class="contact-line web">www.hausarzt-beispielau.de</div>
</body>
</html>
```